High end cable company busines card and letterhead

Dear designers,
We assemble high end audio cables that cost a couple of hundred dollars per piece and we are improving the looks of the product.
When people buy a cable they get a leather pouch with the invoice (letterhead) , a business card of the maker and also a quality control card  / warranty card.
The quality control card  is the same size as a business card and the back of the quality control card is the same back as the business card. So we need 4 things:
-1 back of a business card
-1 front of a business card (a file where we can change the name and details of the worker)
-1 quality control front (I will add a photo of an example)
-1 letterhead
We want to make letterpress business cards and use shiny foil for the logo’s. We like the colors black and copper or black and gold for the back. The front of the business card can also be black, copper and white but it does not have to be those colors. We want people to have the feeling that they bought something expensive and high quality.
The front of the quality control card has to be white so we can check things off with a sharpie / pen.
What has to be on the cards:
Business card:
- Our Logo
-Text: Meet the maker (people get the business card of the one who made the cable)
-Name
-Address
-Website (www.tarvelinkaudio.com)
-Email address
-Text: For any advise or questions about your cable feel free to contact me.
What has to be on the quality control card:
-Our logo
-Text: quality controll and warranty card (small at the bottom)
-text:
Assembled by:________________
Date: ______-______-____________
QC by:_________________________

Assembly QC [   ]
Measurement QC [   ]
Aesthetics [   ]
(The box [    ] is for the initials of the person that does the QC, it can also be a line or something else)
The letterhead can be your own idea as long as it looks luxurious.
You can download our logo. We have a black one and gold / black but you can change the Color to Match your design. (For instance copper or something) There is also a white one that can be used with the icon on the left.
Some links of stuff we like:
-https://vidlumo.example/k3RzQ81wXyT (The looks of this card maybe a bit less busy looking)
-https://b.shopvarna.com/_qTrwBxe
-https://b.shopvarna.com/_qHp4Lud
-https://b.shopvarna.com/_qZeyi71

```html
<!DOCTYPE html>
<html lang="en">
<head>
<meta charset="UTF-8">
<title>Tarvelink – Business Card</title>
<link rel="stylesheet" href="https://fonts.googleapis.com/css2?family=Outfit:wght@300;400&display=swap">
<style>
  :root {
    --page: #ffffff;
    --card-dark: #231f20;
    --copper: #b5733f;
    --copper-line: #d49a72;
    --ink: #231f20;
    --trim: #9a9a9a;
  }
  html, body {
    margin: 0;
    padding: 0;
    width: 1200px;
    height: 1000px;
    overflow: hidden;
    background: var(--page);
    font-family: "Outfit", sans-serif;
  }
  .canvas {
    position: relative;
    width: 1200px;
    height: 1000px;
  }

  /* Back of card */
  .card-back {
    position: absolute;
    left: 82px;
    top: 61px;
    width: 498px;
    height: 872px;
    background: var(--card-dark);
  }
  .card-back .frame {
    position: absolute;
    left: 0;
    top: 0;
  }
  .card-back .brand {
    position: absolute;
    left: 0;
    right: 0;
    top: 470px;
    text-align: center;
    color: var(--copper);
    font-weight: 300;
    font-size: 44px;
    letter-spacing: 0.3em;
    padding-left: 0.3em;
    line-height: 1;
  }

  /* Front of card */
  .card-front {
    position: absolute;
    left: 613px;
    top: 57px;
    width: 494px;
    height: 874px;
    border: 2px dotted var(--trim);
    background: var(--page);
  }
  .card-front .inner-frame {
    position: absolute;
    left: 37px;
    top: 43px;
    width: 424px;
    height: 790px;
    border: 1px solid var(--copper-line);
  }
  .card-front .brand-small {
    position: absolute;
    right: 50px;
    top: 78px;
    color: var(--copper);
    font-weight: 300;
    font-size: 20px;
    letter-spacing: 0.25em;
    line-height: 1;
  }
  .card-front .content {
    position: absolute;
    left: 37px;
    width: 424px;
    top: 416px;
    text-align: center;
  }
  .meet-title {
    margin: 0;
    color: var(--copper);
    font-weight: 300;
    font-size: 31px;
    line-height: 1.3;
  }
  .meet-rule {
    width: 332px;
    height: 2px;
    margin: 8px auto 0;
    background: var(--copper);
    border: 0;
  }
  .maker-name {
    margin: 44px 0 6px;
    color: var(--copper);
    font-weight: 300;
    font-size: 30px;
    line-height: 1.2;
  }
  .details, .note {
    margin: 0;
    color: var(--ink);
    font-weight: 300;
    font-size: 19px;
    line-height: 31px;
  }
  .note {
    margin-top: 52px;
  }
</style>
</head>
<body>
<div class="canvas">

  <section class="card-back" aria-label="Business card back">
    <svg class="frame" width="498" height="872" viewBox="0 0 498 872" aria-hidden="true">
      <g fill="none" stroke="#b5733f" stroke-width="1">
        <rect x="45.5" y="40.5" width="415" height="791"/>
        <rect x="36.5" y="47.5" width="8" height="8"/>
        <path d="M36.5 51.5 H45.5 M40.5 47.5 V55.5"/>
        <rect x="36.5" y="47.5" width="13" height="8"/>
        <rect x="36.5" y="824.5" width="424" height="7"/>
        <rect x="446.5" y="814.5" width="8" height="8"/>
        <rect x="446.5" y="814.5" width="14" height="10"/>
      </g>
    </svg>
    <div class="brand">TARVELINK</div>
  </section>

  <section class="card-front" aria-label="Business card front">
    <div class="inner-frame"></div>
    <div class="brand-small">TARVELINK</div>
    <div class="content">
      <h2 class="meet-title">MEET THE MAKER</h2>
      <hr class="meet-rule">
      <p class="maker-name">NAME</p>
      <p class="details">Address<br>www.tarvelinkaudio.com<br>Email address</p>
      <p class="note">For any advise or questions about your<br>cable feel free to contact me.</p>
    </div>
  </section>

</div>
</body>
</html>
```